Adept Corvana Recruitment company

We require a website for job recruitment company called "Adept Corvana"
Our company is specialising in recruitment of skilled labour from Sri Lanka into Australian market.
We would like to include a job advertising plugin where jobs can be listed and applied for .
COPYWRITING MUST BE INCLUDED !

Industry/Entity Type

Recruitment

Coding

Coded - Design and coding required

Number of Pages Required

5+ page

Colors

Designer to choose colors to be used in the design.

```html
<!DOCTYPE html>
<html lang="en">
<head>
<meta charset="utf-8">
<title>Adept Corvana — Recruitment</title>
<link href="https://fonts.googleapis.com/css2?family=Poppins:wght@400;500;600;700;800&display=swap" rel="stylesheet">
<style>
:root{
  --blue:#0b4fa3;
  --orange:#f6a11c;
  --ink:#555557;
  --ink-dark:#3d3d40;
  --muted:#8a8a8e;
  --soft:#f1f1f2;
  --soft-blue:#e4ebf4;
  --footer:#5b5b5e;
  --white:#ffffff;
  --green:#5a9a4e;
  --red:#e8523f;
}
*{box-sizing:border-box;margin:0;padding:0}
html,body{width:1200px;height:4563px;overflow:hidden}
body{position:relative;background:var(--white);font-family:'Poppins',sans-serif;color:var(--ink)}
.abs{position:absolute}
.brand{font-family:'Poppins',sans-serif;font-weight:700;color:var(--ink-dark);font-size:30px;letter-spacing:.5px;display:flex;align-items:center;gap:10px}
.brand .mark{width:14px;height:14px;background:var(--blue)}
.nav{left:509px;top:44px;display:flex;gap:30px;font-size:11px;color:var(--ink);text-transform:uppercase;align-items:center}
.nav .home{width:16px;height:16px}
.hero-title{left:87px;top:232px;font-size:76px;line-height:80px;font-weight:800;color:var(--ink)}
.hero-sub{left:87px;top:500px;width:440px;font-size:15px;line-height:23px;color:var(--ink)}
.search{left:87px;top:578px;width:663px;height:78px;background:var(--white);border-radius:40px;box-shadow:0 10px 30px rgba(0,0,0,.08);display:flex;align-items:center;font-size:13px;color:var(--ink)}
.search .field{padding-left:28px;width:296px}
.search .field+.field{border-left:1px solid #e3e3e3;height:40px;display:flex;align-items:center}
.search .btn{margin-left:auto;width:151px;height:78px;background:var(--blue);color:var(--white);border-radius:0 40px 40px 0;display:flex;align-items:center;justify-content:center;gap:8px;font-weight:600;font-size:13px}
.photo{border-radius:12px}
.sec-title{left:0;width:1200px;text-align:center;font-size:36px;font-weight:800;color:var(--ink);line-height:46px}
.sec-intro{left:300px;width:600px;text-align:center;font-size:13px;line-height:23px;color:var(--muted)}
.types{left:87px;top:973px;display:flex;gap:11px}
.type{width:196px;height:124px;background:var(--white);border-radius:8px;box-shadow:0 6px 24px rgba(0,0,0,.08);display:flex;flex-direction:column;align-items:center;justify-content:center;gap:14px;font-size:15px;font-weight:600;color:var(--ink)}
.type svg{width:36px;height:36px}
.about-title{left:670px;top:1302px;font-size:36px;font-weight:800;color:var(--ink)}
.about-sub{left:670px;top:1358px;font-size:14px;font-weight:600;color:var(--ink-dark)}
.about-text{left:670px;top:1398px;width:430px;font-size:13.5px;line-height:23px;color:var(--muted)}
.pill-btn{border-radius:24px;color:var(--white);font-size:12px;font-weight:700;display:flex;align-items:center;justify-content:center;text-transform:uppercase}
.jobcard{background:var(--white);border-radius:12px;box-shadow:0 10px 30px rgba(0,0,0,.1)}
.float-card{left:355px;top:1539px;width:258px;height:202px;padding:24px 30px}
.float-card h4{font-size:14.5px;font-weight:600;color:var(--ink-dark);line-height:22px}
.meta{display:flex;gap:14px;font-size:9.5px;color:var(--muted);align-items:center;margin-top:14px}
.meta span{display:flex;align-items:center;gap:5px}
.tag{display:inline-block;font-size:9px;border-radius:10px;padding:2px 12px;margin-top:12px;font-weight:600}
.tag.full{background:#fdf0dc;color:var(--orange)}
.tag.remote{background:#fbe3df;color:var(--red)}
.tag.part{background:#e4f0e1;color:var(--green)}
.tag.online{background:#e2eaf5;color:var(--blue)}
.small-text{font-size:9.5px;line-height:16px;color:var(--muted);margin-top:14px}
.positions{left:87px;top:1959px;display:flex;gap:16px}
.position{width:244px;height:305px;padding:22px 28px}
.position .logo{width:64px;height:64px;border-radius:12px;background:var(--soft);box-shadow:0 4px 12px rgba(0,0,0,.06);display:flex;align-items:center;justify-content:center}
.position .logo i{width:26px;height:26px;border-radius:6px;display:block}
.position h4{font-size:14px;font-weight:600;color:var(--ink-dark);line-height:22px;margin-top:18px}
.position .small-text{font-size:11.5px;line-height:19px}
.stat{width:200px;text-align:center}
.stat .ico{width:86px;height:86px;border-radius:16px;margin:0 auto;display:flex;align-items:center;justify-content:center}
.stat .num{font-size:34px;font-weight:800;color:var(--ink);margin-top:14px;line-height:40px}
.stat .lbl{font-size:15px;color:var(--ink);margin-top:2px}
.cand-title{left:87px;top:2750px;font-size:36px;font-weight:800;color:var(--ink)}
.cand-sub{left:87px;top:2808px;width:330px;font-size:14px;line-height:23px;font-weight:500;color:var(--ink-dark)}
.cand-text{left:87px;top:2874px;width:410px;font-size:13.5px;line-height:23px;color:var(--muted)}
.blogs{left:170px;top:3446px;display:flex;gap:18px}
.blog{width:275px;height:365px;background:var(--white);border-radius:8px;box-shadow:0 8px 26px rgba(0,0,0,.09);overflow:hidden}
.blog .img{height:202px}
.blog .body{padding:20px 24px}
.blog .date{font-size:10.5px;color:var(--muted)}
.blog h4{font-size:15.5px;font-weight:600;color:var(--ink-dark);line-height:21px;margin-top:8px;width:175px}
.blog p{font-size:11px;line-height:19px;color:var(--muted);margin-top:12px}
.footer{left:0;top:4020px;width:1200px;height:543px;background:var(--footer);border-top-right-radius:195px}
.cta{left:179px;top:3924px;width:840px;height:188px;background:var(--blue);border-radius:94px}
.cta h2{position:absolute;left:74px;top:42px;font-size:42px;line-height:54px;font-weight:800;color:var(--white)}
.cta .btn{position:absolute;left:601px;top:71px;width:182px;height:45px;background:var(--white);color:var(--ink-dark);border-radius:10px;font-size:11px;font-weight:700;display:flex;align-items:center;justify-content:center}
.f-brand{left:101px;top:4250px;color:var(--white);font-size:34px}
.socials{left:127px;top:4344px;display:flex;gap:13px}
.socials i{width:40px;height:40px;border-radius:50%;background:#6e6e72;display:block}
.f-col h5{font-size:19px;font-weight:600;color:var(--white);margin-bottom:22px}
.f-col li{list-style:none;font-size:12.5px;color:#e4e4e6;line-height:31px}
.f-col li::before{content:"›";margin-right:8px}
.contact-item{display:flex;gap:10px;font-size:12.5px;color:#e4e4e6;line-height:18px;margin-bottom:18px}
.contact-item svg{flex:none;margin-top:2px}
.news p{font-size:12.5px;color:#e4e4e6;line-height:18px;width:240px}
.news .input{margin-top:20px;width:259px;height:43px;background:var(--white);border-radius:22px;display:flex;align-items:center;padding:0 18px;font-size:11px;color:var(--muted);gap:8px}
.news .input svg:last-child{margin-left:auto}
.divider{left:0;top:4505px;width:1200px;height:1px;background:rgba(255,255,255,.15)}
.copyright{left:0;top:4522px;width:1200px;text-align:center;font-size:12px;font-weight:600;color:var(--white)}
.to-top{left:1132px;top:4480px;width:44px;height:44px;border-radius:50%;background:var(--white);display:flex;align-items:center;justify-content:center}
</style>
</head>
<body>

<!-- Header -->
<div class="abs brand" style="left:87px;top:38px"><span class="mark"></span>Adept Corvana</div>
<nav class="abs nav">
  <svg class="home" viewBox="0 0 16 16"><path d="M2 8 8 2l6 6h-2v6H9v-4H7v4H4V8z" fill="var(--blue)"/></svg>
  <span>About</span><span>Client Services</span><span>Request Services</span><span>Industries</span><span>Blog</span><span>Contact</span>
</nav>

<!-- Hero decoration -->
<svg class="abs" style="left:620px;top:100px" width="580" height="760" viewBox="0 0 580 760">
  <path d="M48 6h200v680H48a20 20 0 0 1-20-20V206A200 200 0 0 1 48 6z" fill="var(--soft)"/>
  <circle cx="360" cy="210" r="200" fill="var(--soft)"/>
  <circle cx="370" cy="460" r="230" fill="var(--soft)"/>
  <path d="M169 6h118v116A118 118 0 0 1 169 6z" fill="var(--blue)"/>
  <path d="M580 255v141H451A141 141 0 0 1 580 255z" fill="var(--blue)"/>
  <path d="M451 396h129v137A137 137 0 0 0 451 396z" fill="#5d5d60"/>
</svg>
<div class="abs photo" role="img" aria-label="Three colleagues smiling while working together at a laptop" style="left:665px;top:222px;width:406px;height:519px;background:linear-gradient(150deg,#7a6a5e,#3f3a3a 55%,#6a7c8e)"></div>

<h1 class="abs hero-title">Get your<br>dream job<br>today</h1>
<p class="abs hero-sub">Our company is specializing in recruitment of skilled labour from Sri Lanka into Australian market.</p>
<div class="abs search">
  <div class="field">Search title or keyword</div>
  <div class="field">New York</div>
  <div class="btn"><svg width="15" height="15" viewBox="0 0 16 16"><circle cx="7" cy="7" r="5" stroke="#fff" stroke-width="2" fill="none"/><path d="m11 11 4 4" stroke="#fff" stroke-width="2"/></svg>SEARCH</div>
</div>

<!-- Trending job types -->
<h2 class="abs sec-title" style="top:838px">Trending Job Types</h2>
<p class="abs sec-intro" style="top:898px">Aenean sollicitudin, lorem quis bibendum auctor nisi elit consequat ipsum nec sagittis sem nibh id elit. Duis sed odio sit amet nibh vulputate cursus a sit.</p>
<div class="abs types">
  <div class="type"><svg viewBox="0 0 36 36"><path d="M4 18 18 5l14 13h-4v13h-7v-8h-6v8H8V18z" fill="var(--orange)"/></svg>From Home Job</div>
  <div class="type"><svg viewBox="0 0 36 36"><circle cx="18" cy="18" r="14" fill="var(--red)"/><path d="M4 18h28M18 4c-6 8-6 20 0 28M18 4c6 8 6 20 0 28" stroke="#fff" stroke-width="2" fill="none"/></svg>Online Job</div>
  <div class="type"><svg viewBox="0 0 36 36"><circle cx="18" cy="18" r="14" fill="var(--green)"/><path d="M18 9v10h7" stroke="#fff" stroke-width="2.5" fill="none"/></svg>Full Time Job</div>
  <div class="type"><svg viewBox="0 0 36 36"><circle cx="18" cy="18" r="14" fill="#3f5fd4"/><path d="M18 9v10h7" stroke="#fff" stroke-width="2.5" fill="none"/></svg>Part Time Job</div>
  <div class="type"><svg viewBox="0 0 36 36"><rect x="6" y="6" width="24" height="24" rx="5" stroke="var(--orange)" stroke-width="3" fill="none"/><path d="M11 15h14M11 21h14" stroke="var(--orange)" stroke-width="3"/></svg>Virtual Job</div>
</div>

<!-- About -->
<svg class="abs" style="left:100px;top:1159px" width="80" height="155"><path d="M78 0v153A77 77 0 0 1 78 0z" fill="var(--soft-blue)"/></svg>
<div class="abs" role="img" aria-label="Two professionals shaking hands in an office" style="left:138px;top:1216px;width:422px;height:480px;border-radius:0 0 0 150px;background:linear-gradient(160deg,#b9b2a8,#6a5a52 55%,#4a4a50)"></div>
<div class="abs jobcard float-card">
  <h4>Senior Designer, UX &amp; UI, Mobile App</h4>
  <div class="meta"><span><svg width="9" height="11" viewBox="0 0 10 12"><path d="M5 12S1 7 1 4.5a4 4 0 0 1 8 0C9 7 5 12 5 12z" fill="#9aa"/></svg>New York, NY</span><span><svg width="10" height="10"><rect width="10" height="10" rx="2" fill="#8aa0c8"/></svg>Harlow &amp; Finch</span></div>
  <span class="tag full">Full Time</span>
  <p class="small-text" style="font-size:8.5px;line-height:15px">Senior Product Designer (UX/UI) About Lumora. Lumora is an experiential platform that empowers the</p>
</div>
<h2 class="abs about-title">About  Keen Folks</h2>
<p class="abs about-sub">We Help Candidates Find Their Next Great Opportunity</p>
<p class="abs about-text">Aenean sollicitudin, lorem quis bibendum auctor, nisi elit consequat ipsum, nec sagittis sem nibh id elit. Duis sed odio sit amet nibh vulputate cursus a sit amet mauris. Morbi accumsan ipsum velit. Nam nec tellus a tincidunt auctor a ornare odio. Sed non  mauris vitae erat consequat auctor eu in elit. Class aptent taciti sociosqu ad litora torquent per conubia nostra...</p>
<div class="abs pill-btn" style="left:670px;top:1585px;width:156px;height:44px;background:var(--blue)">Find Out More</div>

<!-- Trending positions -->
<svg class="abs" style="left:868px;top:1822px" width="160" height="78"><path d="M0 76A80 76 0 0 1 160 76z" fill="var(--soft)"/></svg>
<svg class="abs" style="left:993px;top:1861px" width="207" height="505"><path d="M0 0A252 252 0 0 1 0 505h207V0z" fill="var(--soft-blue)"/></svg>
<h2 class="abs sec-title" style="top:1826px">Need to Hire?<br>Trending Job Positions</h2>
<div class="abs positions">
  <div class="jobcard position">
    <div class="logo"><i style="background:#c94b7a"></i></div>
    <h4>Senior Product Designer (UIUX) Job</h4>
    <div class="meta"><span>⦿ New York, NY</span><span>▪ Company</span></div>
    <span class="tag full">Full Time</span>
    <p class="small-text">Aenean lorem quis bibendum auctorpsum nec sagittis sem nibh id elit duis sed ...</p>
  </div>
  <div class="jobcard position">
    <div class="logo"><i style="background:#2f7fd6;border-radius:50%"></i></div>
    <h4>Java Developer Infrastructure Service</h4>
    <div class="meta"><span>⦿ New York, NY</span><span>▪ Company</span></div>
    <span class="tag remote">Remote</span>
    <p class="small-text">Aenean lorem quis bibendum auctorpsum nec sagittis sem nibh id elit duis sed ...</p>
  </div>
  <div class="jobcard position">
    <div class="logo"><i style="background:#9b4fc9;border-radius:50%"></i></div>
    <h4>Core Java Developer Big Data</h4>
    <div class="meta"><span>⦿ New York, NY</span><span>▪ Company</span></div>
    <span class="tag part">Part Time</span>
    <p class="small-text">Aenean lorem quis bibendum auctorpsum nec sagittis sem nibh id elit duis sed ...</p>
  </div>
  <div class="jobcard position">
    <div class="logo"><i style="background:#3aa7a0"></i></div>
    <h4>Senior Designer UX &amp; UI Mobile App</h4>
    <div class="meta"><span>⦿ New York, NY</span><span>▪ Company</span></div>
    <span class="tag online">Online</span>
    <p class="small-text">Aenean lorem quis bibendum auctorpsum nec sagittis sem nibh id elit duis sed ...</p>
  </div>
</div>

<!-- Stats -->
<div class="abs stat" style="left:263px;top:2357px">
  <div class="ico" style="background:#5b5b5e"><svg width="38" height="38" viewBox="0 0 38 38" fill="none" stroke="#fff" stroke-width="2.4"><rect x="5" y="11" width="28" height="20" rx="3"/><path d="M14 11V7h10v4M5 19h28M17 19v3h4v-3"/></svg></div>
  <div class="num">50k+</div><div class="lbl">Job Vacancy</div>
</div>
<div class="abs stat" style="left:492px;top:2357px">
  <div class="ico" style="background:var(--blue)"><svg width="38" height="38" viewBox="0 0 38 38" fill="none" stroke="#fff" stroke-width="2.4"><circle cx="19" cy="13" r="7"/><path d="M6 34c0-8 6-12 13-12s13 4 13 12"/></svg></div>
  <div class="num">20k+</div><div class="lbl">People Got Hired</div>
</div>
<div class="abs stat" style="left:721px;top:2357px">
  <div class="ico" style="background:#5b5b5e"><svg width="38" height="38" viewBox="0 0 38 38" fill="none" stroke="#fff" stroke-width="2.4"><path d="M8 33V6h16v27M24 14h7v19M5 33h29M12 11h2M18 11h2M12 17h2M18 17h2M12 23h2M18 23h2"/></svg></div>
  <div class="num">2k+</div><div class="lbl">Our Companies</div>
</div>

<!-- Candidates -->
<svg class="abs" style="left:151px;top:2614px" width="154" height="78"><path d="M0 0h154A77 77 0 0 1 0 0z" fill="var(--soft)"/></svg>
<h2 class="abs cand-title">Our Candidates</h2>
<p class="abs cand-sub">71% of candidates increased their salary when they found a job</p>
<p class="abs cand-text">Aenean sollicitudin, lorem quis bibendum auctor, nisi elit consequat ipsum, nec sagittis sem nibh id elit. Duis sed odio sit amet nibh vulputate cursus a sit amet mauris. Morbi accumsan ipsum velit. Nam nec tellus a tincidunt auctor a ornare odio. Sed non  mauris...</p>
<div class="abs pill-btn" style="left:87px;top:3015px;width:200px;height:44px;background:var(--orange)">View All Candidates</div>
<div class="abs" role="img" aria-label="Portrait of a young man in a dark suit" style="left:861px;top:2606px;width:249px;height:308px;border-radius:14px 14px 14px 0;background:linear-gradient(180deg,#d9d9db,#b9b9bd 55%,#2a3550)"></div>
<div class="abs" role="img" aria-label="Portrait of a smiling man in a grey suit giving a thumbs up" style="left:562px;top:2765px;width:333px;height:383px;border-radius:20px 20px 20px 0;background:linear-gradient(180deg,#cfcfd1,#b4b4b7 60%,#8c8c90)"></div>
<svg class="abs" style="left:1040px;top:3190px" width="60" height="56"><path d="M0 56A56 56 0 0 1 56 0v56z" fill="var(--soft-blue)"/></svg>
<div class="abs" role="img" aria-label="Portrait of a smiling young woman in a white shirt" style="left:860px;top:3061px;width:182px;height:223px;border-radius:14px 14px 0 14px;background:linear-gradient(180deg,#c7c7c9,#e7ddd2 60%,#2e2e34)"></div>

<!-- Blog -->
<h2 class="abs sec-title" style="top:3306px">Latest Blog Post</h2>
<p class="abs sec-intro" style="top:3370px">Aenean sollicitudin, lorem quis bibendum auctor nisi elit consequat ipsum nec sagittis sem nibh id elit. Duis sed odio sit amet nibh vulputate cursus a sit.</p>
<div class="abs blogs">
  <article class="blog">
    <div class="img" role="img" aria-label="Team meeting around a table in a bright office" style="background:linear-gradient(150deg,#6c6a66,#a99a86 50%,#3b3e48)"></div>
    <div class="body"><div class="date">25-02-2022</div><h4>Some event heading goes here</h4><p>Aenean sollicitudin lorem bibendum auctor nisi elit consequat ipsum...</p></div>
  </article>
  <article class="blog">
    <div class="img" role="img" aria-label="Smiling man with arms crossed in an open office" style="background:linear-gradient(150deg,#d2cfc9,#8a8680 55%,#3f4e6a)"></div>
    <div class="body"><div class="date">25-02-2022</div><h4>Some event heading goes here</h4><p>Aenean sollicitudin lorem bibendum auctor nisi elit consequat ipsum...</p></div>
  </article>
  <article class="blog">
    <div class="img" role="img" aria-label="Colleagues talking in a modern glass office" style="background:linear-gradient(150deg,#9aa6ae,#6c6560 55%,#c8c2b8)"></div>
    <div class="body"><div class="date">25-02-2022</div><h4>Some event heading goes here</h4><p>Aenean sollicitudin lorem bibendum auctor nisi elit consequat ipsum...</p></div>
  </article>
</div>

<!-- Footer -->
<footer class="abs footer"></footer>
<div class="abs cta">
  <h2>Start Building Your<br>Event Today With Me!</h2>
  <div class="btn">MY EVENT PLANNER</div>
</div>

<div class="abs brand f-brand"><span class="mark" style="background:var(--white)"></span>Adept Corvana</div>
<div class="abs socials"><i></i><i></i><i></i><i></i></div>

<div class="abs f-col" style="left:418px;top:4208px">
  <h5>Quick links</h5>
  <ul><li>About</li><li>Client Services</li><li>Request Services</li><li>Industries</li><li>Blog</li><li>Contact</li></ul>
</div>
<div class="abs f-col" style="left:603px;top:4208px">
  <h5>Contact info</h5>
  <div class="contact-item"><svg width="13" height="10" viewBox="0 0 13 10"><rect x=".5" y=".5" width="12" height="9" fill="none" stroke="#ccc"/><path d="m1 1 5.5 4L12 1" fill="none" stroke="#ccc"/></svg><span>Email:<br>hello@adeptcorvana.example</span></div>
  <div class="contact-item"><svg width="12" height="12" viewBox="0 0 12 12"><path d="M2 1h3l1 3-2 1a7 7 0 0 0 3 3l1-2 3 1v3c-5 1-10-4-9-9z" fill="#ccc"/></svg><span>Phone:<br>+00 100 200 3000</span></div>
  <div class="contact-item"><svg width="11" height="13" viewBox="0 0 10 12"><path d="M5 12S1 7 1 4.5a4 4 0 0 1 8 0C9 7 5 12 5 12z" fill="#ccc"/></svg><span>Location:<br>Some address line here<br>Sample Town 00000</span></div>
</div>
<div class="abs f-col news" style="left:851px;top:4208px">
  <h5>Newsletter</h5>
  <p>Subscribe to our email address to get the latest news.</p>
  <div class="input"><svg width="12" height="9"><rect x=".5" y=".5" width="11" height="8" fill="none" stroke="#aaa"/></svg>Enter Your Email...<svg width="16" height="16" viewBox="0 0 16 16"><path d="M1 7 15 1 10 15 8 9z" fill="var(--blue)"/></svg></div>
</div>

<div class="abs divider"></div>
<div class="abs to-top"><svg width="14" height="14" viewBox="0 0 14 14"><path d="M7 12V2M3 6l4-4 4 4" stroke="var(--ink)" stroke-width="1.5" fill="none"/></svg></div>
<p class="abs copyright">© Copyright 2022, All Rights Reserved</p>

</body>
</html>
```